Need a stunning looking Business Card Design for my Telecom Business, Wow FACTOR!

I deal with high level IT Directors , and Contractors.
I need to impress them with a sleek , professional and unique business card.
Im thinking options as far as rounded edges, plastic , or even metal card or die cut on a corner.
Whatever looks better and leave an unforgettable first impression.
im looking for the wow factor.
Front should have the basics info (attached on the picture of current business card)
i would like to add picture of myself somewhere
Back side
should have logo and maybe some pictures or past projects, you can download from my website ( www.lumvexholdings.com)

```html
<!DOCTYPE html>
<html lang="en">
<head>
<meta charset="utf-8">
<title>Lumvex Holdings – Business Card</title>
<link href="https://fonts.googleapis.com/css2?family=Lato:wght@400;700;900&display=swap" rel="stylesheet">
<style>
  :root {
    --backdrop: #cdcdcd;
    --card-white: #ffffff;
    --card-navy: #18234f;
    --ink-navy: #1b2a5c;
    --ink-blue: #1f86c8;
    --ink-cyan: #27a9e1;
    --ink-grey: #3f3f46;
    --rule-grey: #8a8a8a;
    --photo-frame: #2a3a78;
  }
  * { margin: 0; padding: 0; box-sizing: border-box; }
  html, body { width: 1200px; height: 800px; overflow: hidden; }
  body {
    background: var(--backdrop);
    font-family: "Lato", Arial, sans-serif;
    position: relative;
  }
  .card {
    position: absolute;
    left: 423px;
    width: 419px;
    height: 239px;
    border-radius: 12px;
    overflow: hidden;
  }
  .card--front { top: 130px; background: var(--card-white); color: var(--ink-grey); }
  .card--back { top: 430px; background: var(--card-navy); }

  .portrait {
    position: absolute;
    left: 23px; top: 21px;
    width: 63px; height: 70px;
    border: 1px solid var(--photo-frame);
    background: linear-gradient(180deg, #f2f2f2 0%, #d9d9dc 55%, #8c8f99 100%);
  }
  .holder-name {
    position: absolute;
    left: 23px; top: 104px;
    font-size: 19px; font-weight: 900;
    letter-spacing: -0.2px;
    color: var(--ink-navy);
  }
  .holder-name .surname {
    font-weight: 700;
    background: linear-gradient(90deg, var(--ink-blue), #35b4ea);
    -webkit-background-clip: text; background-clip: text;
    color: transparent;
  }
  .holder-role {
    position: absolute;
    left: 23px; top: 128px;
    font-size: 11px;
  }
  .divider {
    position: absolute;
    left: 23px; right: 22px; top: 148px;
    border-top: 1px solid var(--rule-grey);
  }
  .contact-list {
    position: absolute;
    left: 23px; top: 156px;
    list-style: none;
    font-size: 11px;
    line-height: 14px;
  }
  .contact-list li { display: flex; align-items: center; gap: 8px; }
  .contact-list svg { width: 11px; height: 11px; flex: none; }
  .company-note {
    position: absolute;
    right: 22px; top: 180px;
    text-align: right;
    font-size: 11px;
    line-height: 15px;
  }
  .brand {
    position: absolute;
    display: flex; align-items: center; gap: 7px;
    font-weight: 700;
    letter-spacing: 1px;
    white-space: nowrap;
  }
  .brand-dot { border-radius: 50%; flex: none; }
  .card--front .brand { right: 22px; top: 58px; font-size: 15px; color: var(--ink-navy); }
  .card--front .brand-dot { width: 14px; height: 14px; background: var(--ink-blue); }
  .card--back .brand {
    left: 0; right: 0; top: 112px; justify-content: center;
    font-size: 22px; color: #ffffff;
  }
  .card--back .brand-dot { width: 20px; height: 20px; background: var(--ink-cyan); }
  .office-band {
    position: absolute;
    left: 70px; right: 70px; top: 204px;
    height: 17px;
    background: linear-gradient(90deg, rgba(31,134,200,0) 0%, #1f7fc0 18%, #2592d2 50%, #1f7fc0 82%, rgba(31,134,200,0) 100%);
    text-align: center;
    font-size: 10.5px;
    line-height: 17px;
    color: var(--card-navy);
  }
</style>
</head>
<body>
  <section class="card card--front">
    <div class="portrait" role="img" aria-label="Portrait photo of the card holder"></div>
    <div class="brand"><span class="brand-dot"></span>LUMVEX HOLDINGS</div>
    <h1 class="holder-name">DANIEL <span class="surname">OKAFOR</span></h1>
    <p class="holder-role">Operations Manager</p>
    <div class="divider"></div>
    <ul class="contact-list">
      <li><svg viewBox="0 0 24 24"><path fill="#27a9e1" d="M6.6 10.8a15 15 0 0 0 6.6 6.6l2.2-2.2a1 1 0 0 1 1-.25 11 11 0 0 0 3.6.6 1 1 0 0 1 1 1V20a1 1 0 0 1-1 1A17 17 0 0 1 3 4a1 1 0 0 1 1-1h3.5a1 1 0 0 1 1 1c0 1.25.2 2.45.6 3.6a1 1 0 0 1-.25 1z"/></svg>(305) 555-0147 (Miami)</li>
      <li><svg viewBox="0 0 24 24"><path fill="#27a9e1" d="M6.6 10.8a15 15 0 0 0 6.6 6.6l2.2-2.2a1 1 0 0 1 1-.25 11 11 0 0 0 3.6.6 1 1 0 0 1 1 1V20a1 1 0 0 1-1 1A17 17 0 0 1 3 4a1 1 0 0 1 1-1h3.5a1 1 0 0 1 1 1c0 1.25.2 2.45.6 3.6a1 1 0 0 1-.25 1z"/></svg>(954) 555-0182 (Broward)</li>
      <li><svg viewBox="0 0 24 24"><path fill="#27a9e1" d="M6.6 10.8a15 15 0 0 0 6.6 6.6l2.2-2.2a1 1 0 0 1 1-.25 11 11 0 0 0 3.6.6 1 1 0 0 1 1 1V20a1 1 0 0 1-1 1A17 17 0 0 1 3 4a1 1 0 0 1 1-1h3.5a1 1 0 0 1 1 1c0 1.25.2 2.45.6 3.6a1 1 0 0 1-.25 1z"/></svg>(561) 555-0139 (Palm Beach)</li>
      <li><svg viewBox="0 0 24 24"><rect x="2" y="5" width="20" height="14" fill="#27a9e1"/><path d="M2 5l10 8 10-8M2 19l7-7M22 19l-7-7" stroke="#fff" stroke-width="1.6" fill="none"/></svg>info@lumvexholdings.com</li>
      <li><svg viewBox="0 0 24 24" fill="none" stroke="#27a9e1" stroke-width="1.8"><circle cx="12" cy="12" r="10"/><ellipse cx="12" cy="12" rx="4.5" ry="10"/><path d="M2 12h20M4 7h16M4 17h16"/></svg>www.lumvexholdings.com</li>
    </ul>
    <p class="company-note">Low Voltage Contractor<br>Offices in Miami,<br>Broward and Palm Beach</p>
  </section>

  <section class="card card--back">
    <div class="brand"><span class="brand-dot"></span>LUMVEX HOLDINGS</div>
    <div class="office-band">Miami&nbsp; || &nbsp;Fort Lauderdale&nbsp; || &nbsp;Palm Beach</div>
  </section>
</body>
</html>
```